Moss Harbor Probiotic Chews label design to be used on a jar

I want to design a label for probiotic chews packaging. The jar is black with black lid. Jar and label dims attached. I also have created 2 draft designs. I do not want you to use them as inspiration, but it tells you product name and key features in text form. e.g. blue on gold & black design is there so that when we produce a different chew e.g. for joint support, we can color code it with product name to make them similar, but distinct. The KEY feature is to have it stand out in search results. It needs to POP. It has to be bright, colorful and not the same as everything else. There is more information that goes on the "back" of the label, but for the purpose of this project I only care about the "font". You do not need to design the whole label - I just want to see a mock up of the front - we will fill in the other details later.

Target Market(s)

Dog owners in the USA who are interested in detail, but are drawn by emotion

Industry/Entity Type

Functional dog treats / supplements

Font styles to use
Other font styles liked:
• something like https://www.typevane.net/plain-curve.font

Colors
0094D4
00A9DD
6FCCEA
C7EBF8
E9F6FB

Requirements
Must have
• Large title readable on mobile in search results (depending on your choice of style) either "Probiotics & Enzymes for Dogs" or "Lively Wag Chews", elements visible in the examples I provided.
Nice to have
• bright, vivid color that will make the package stand out, focus on important features, but also ability to expand to other products by adjusting the color palette for e.g. hip & join supplement
Should not have
• Cannot be too busy, unclear

```html
<!DOCTYPE html>
<html lang="en">
<head>
<meta charset="UTF-8">
<title>Moss Harbor Probiotic Chews – Front Labels</title>
<link href="https://fonts.googleapis.com/css2?family=Fredoka:wght@500;600;700&family=Varela+Round&display=swap" rel="stylesheet">
<style>
  :root {
    --page-bg: #e4e4e4;
    --blue-label: #2f86d8;
    --blue-label-dark: #1f6fc0;
    --red-label: #d9232b;
    --red-label-dark: #b8151d;
    --white: #ffffff;
    --check-yellow: #f4d21f;
    --flavor-yellow: #f6e21a;
    --fur-light: #e2b67c;
    --fur-dark: #a8713a;
    --chew-light: #c06a33;
    --chew-dark: #7f3c19;
  }
  * { margin: 0; padding: 0; box-sizing: border-box; }
  html, body {
    width: 1200px; height: 900px; overflow: hidden;
    background: radial-gradient(ellipse at 50% 35%, #f0f0f0 0%, var(--page-bg) 70%);
  }
  .canvas { position: relative; width: 1200px; height: 900px; }
  .label {
    position: absolute; top: 345px;
    width: 400px; height: 330px;
    overflow: hidden; color: var(--white);
    font-family: "Varela Round", sans-serif;
  }
  .label--blue { left: 165px; background: linear-gradient(180deg, var(--blue-label) 0%, var(--blue-label-dark) 100%); }
  .label--red  { left: 635px; background: linear-gradient(180deg, var(--red-label) 0%, var(--red-label-dark) 100%); }
  .dog-photo {
    position: absolute; left: 10px; top: 22px;
    width: 150px; height: 308px;
    border-radius: 70px 70px 0 0;
    background: radial-gradient(ellipse at 50% 30%, var(--fur-light) 0%, #c98f52 55%, var(--fur-dark) 100%);
  }
  .brand {
    position: absolute; left: 165px; top: 26px; width: 230px;
    display: flex; align-items: center; justify-content: center; gap: 7px;
    font-family: "Fredoka", sans-serif; font-weight: 600;
    font-size: 26px; line-height: 32px; white-space: nowrap;
    text-transform: uppercase;
  }
  .brand-dot { width: 10px; height: 10px; border-radius: 50%; background: var(--white); flex: none; }
  .title {
    position: absolute; left: 165px; top: 72px; width: 230px;
    text-align: center; font-family: "Fredoka", sans-serif; font-weight: 700;
    text-transform: uppercase; line-height: 1; white-space: nowrap;
  }
  .title-line { display: block; font-size: 38px; transform: rotate(4deg); }
  .title-line + .title-line { font-size: 42px; margin-top: 4px; transform: rotate(-3deg); }
  .benefits {
    position: absolute; left: 176px; top: 188px; list-style: none;
    font-size: 14px; line-height: 20px; white-space: nowrap;
  }
  .benefits li { display: flex; align-items: center; gap: 6px; }
  .benefits svg { width: 12px; height: 12px; flex: none; }
  .count { position: absolute; left: 200px; top: 302px; font-size: 14px; line-height: 18px; }
  .chew-photo {
    position: absolute; left: 322px; top: 182px; width: 46px; height: 42px;
    border-radius: 9px;
    background: linear-gradient(145deg, var(--chew-light) 0%, var(--chew-dark) 100%);
  }
  .flavor {
    position: absolute; left: 312px; top: 230px; width: 72px;
    text-align: center; color: var(--flavor-yellow);
    font-family: "Fredoka", sans-serif; font-weight: 600; font-size: 13px; line-height: 15px;
  }
  .flavor-arrow { position: absolute; left: 374px; top: 190px; width: 18px; height: 40px; }
  .made-in {
    position: absolute; left: 318px; top: 296px;
    display: flex; align-items: center; gap: 4px;
  }
  .made-in-flag { width: 24px; height: 16px; background: var(--white); border-radius: 2px; }
  .made-in-text { font-family: "Fredoka", sans-serif; font-weight: 600; line-height: 1; }
  .made-in-text small { display: block; font-size: 6px; }
  .made-in-text strong { display: block; font-size: 13px; }
</style>
</head>
<body>
<main class="canvas">

  <section class="label label--blue" aria-label="Moss Harbor Probiotic Chews label, blue">
    <div class="dog-photo" role="img" aria-label="Photo of a smiling golden retriever"></div>
    <div class="brand"><span class="brand-dot"></span>Moss Harbor</div>
    <h1 class="title"><span class="title-line">Probiotic</span><span class="title-line">Chews</span></h1>
    <ul class="benefits">
      <li><svg viewBox="0 0 12 12"><circle cx="6" cy="6" r="5.2" fill="none" stroke="#f4d21f" stroke-width="1.2"/><path d="M3.4 6.2l1.8 1.7 3.4-3.6" fill="none" stroke="#f4d21f" stroke-width="1.4" stroke-linecap="round" stroke-linejoin="round"/></svg>No More Gas</li>
      <li><svg viewBox="0 0 12 12"><circle cx="6" cy="6" r="5.2" fill="none" stroke="#f4d21f" stroke-width="1.2"/><path d="M3.4 6.2l1.8 1.7 3.4-3.6" fill="none" stroke="#f4d21f" stroke-width="1.4" stroke-linecap="round" stroke-linejoin="round"/></svg>Better Poop</li>
      <li><svg viewBox="0 0 12 12"><circle cx="6" cy="6" r="5.2" fill="none" stroke="#f4d21f" stroke-width="1.2"/><path d="M3.4 6.2l1.8 1.7 3.4-3.6" fill="none" stroke="#f4d21f" stroke-width="1.4" stroke-linecap="round" stroke-linejoin="round"/></svg>Loved By Dogs</li>
      <li><svg viewBox="0 0 12 12"><circle cx="6" cy="6" r="5.2" fill="none" stroke="#f4d21f" stroke-width="1.2"/><path d="M3.4 6.2l1.8 1.7 3.4-3.6" fill="none" stroke="#f4d21f" stroke-width="1.4" stroke-linecap="round" stroke-linejoin="round"/></svg>Healthy Tummy</li>
      <li><svg viewBox="0 0 12 12"><circle cx="6" cy="6" r="5.2" fill="none" stroke="#f4d21f" stroke-width="1.2"/><path d="M3.4 6.2l1.8 1.7 3.4-3.6" fill="none" stroke="#f4d21f" stroke-width="1.4" stroke-linecap="round" stroke-linejoin="round"/></svg>Vet Formulated</li>
    </ul>
    <div class="chew-photo" role="img" aria-label="Photo of two beef liver chews"></div>
    <svg class="flavor-arrow" viewBox="0 0 18 40"><path d="M3 37 C13 32 15 19 8 7" fill="none" stroke="#fff" stroke-width="1.5" stroke-linecap="round"/><path d="M4.5 10 L8 5 L12 10" fill="none" stroke="#fff" stroke-width="1.5" stroke-linecap="round" stroke-linejoin="round"/></svg>
    <p class="flavor">Beef Liver<br>Flavor</p>
    <p class="count">170 Chews</p>
    <div class="made-in"><span class="made-in-flag"></span><span class="made-in-text"><small>MADE IN</small><strong>USA</strong></span></div>
  </section>

  <section class="label label--red" aria-label="Moss Harbor Probiotic Chews label, red">
    <div class="dog-photo" role="img" aria-label="Photo of a smiling golden retriever"></div>
    <div class="brand"><span class="brand-dot"></span>Moss Harbor</div>
    <h2 class="title"><span class="title-line">Probiotic</span><span class="title-line">Chews</span></h2>
    <ul class="benefits">
      <li><svg viewBox="0 0 12 12"><circle cx="6" cy="6" r="5.2" fill="none" stroke="#f4d21f" stroke-width="1.2"/><path d="M3.4 6.2l1.8 1.7 3.4-3.6" fill="none" stroke="#f4d21f" stroke-width="1.4" stroke-linecap="round" stroke-linejoin="round"/></svg>No More Gas</li>
      <li><svg viewBox="0 0 12 12"><circle cx="6" cy="6" r="5.2" fill="none" stroke="#f4d21f" stroke-width="1.2"/><path d="M3.4 6.2l1.8 1.7 3.4-3.6" fill="none" stroke="#f4d21f" stroke-width="1.4" stroke-linecap="round" stroke-linejoin="round"/></svg>Better Poop</li>
      <li><svg viewBox="0 0 12 12"><circle cx="6" cy="6" r="5.2" fill="none" stroke="#f4d21f" stroke-width="1.2"/><path d="M3.4 6.2l1.8 1.7 3.4-3.6" fill="none" stroke="#f4d21f" stroke-width="1.4" stroke-linecap="round" stroke-linejoin="round"/></svg>Loved By Dogs</li>
      <li><svg viewBox="0 0 12 12"><circle cx="6" cy="6" r="5.2" fill="none" stroke="#f4d21f" stroke-width="1.2"/><path d="M3.4 6.2l1.8 1.7 3.4-3.6" fill="none" stroke="#f4d21f" stroke-width="1.4" stroke-linecap="round" stroke-linejoin="round"/></svg>Healthy Tummy</li>
      <li><svg viewBox="0 0 12 12"><circle cx="6" cy="6" r="5.2" fill="none" stroke="#f4d21f" stroke-width="1.2"/><path d="M3.4 6.2l1.8 1.7 3.4-3.6" fill="none" stroke="#f4d21f" stroke-width="1.4" stroke-linecap="round" stroke-linejoin="round"/></svg>Vet Formulated</li>
    </ul>
    <div class="chew-photo" role="img" aria-label="Photo of two beef liver chews"></div>
    <svg class="flavor-arrow" viewBox="0 0 18 40"><path d="M3 37 C13 32 15 19 8 7" fill="none" stroke="#fff" stroke-width="1.5" stroke-linecap="round"/><path d="M4.5 10 L8 5 L12 10" fill="none" stroke="#fff" stroke-width="1.5" stroke-linecap="round" stroke-linejoin="round"/></svg>
    <p class="flavor">Beef Liver<br>Flavor</p>
    <p class="count">170 Chews</p>
    <div class="made-in"><span class="made-in-flag"></span><span class="made-in-text"><small>MADE IN</small><strong>USA</strong></span></div>
  </section>

</main>
</body>
</html>
```